Whimsical Flyer for Children's Storytime at Glow And Grow

Design an 8 1/2 by 11 color flyer to promote a storytime series at our store. At Glow And Grow we believe that the shortest distance between two people is a story. Everything in our store has a story behind it and now we are excited to have one of the world’s best storytellers coming to share her gifts with kids ages 2-5, once a week, starting at 10am on July 7th for an eight-week series. Ms. Dolores (Pemberley), children’s librarian and storyteller extraordinaire, and our own Mr. Toby, her budding apprentice, will regale children with music, stories and movement, FREE! 10am. Reservations required. Visit glowandgrow.example for details. 872 E. 61st Street - San Mateo CA 94417.

Target Market(s)

Parents and caregivers with children

Requirements
Must have
• Whimsy, fun, enticing to parents and children

```html
<!DOCTYPE html>
<html lang="en">
<head>
<meta charset="utf-8">
<title>Storytime at Glow And Grow</title>
<link href="https://fonts.googleapis.com/css2?family=Emilys+Candy&family=Amatic+SC:wght@700&family=Open+Sans:wght@400;600;700&display=swap" rel="stylesheet">
<style>
  :root {
    --orange: #d9682a;
    --orange-deep: #c95a22;
    --orange-soft: #e07a3c;
    --olive: #8c9a3c;
    --olive-light: #cfd69b;
    --peach: #f7d3a1;
    --cream: #fbeedd;
    --white: #ffffff;
  }
  * { margin: 0; padding: 0; box-sizing: border-box; }
  html, body { width: 933px; height: 1200px; overflow: hidden; background: var(--white); }
  .flyer {
    position: relative;
    width: 933px;
    height: 1200px;
    overflow: hidden;
    background: var(--orange);
    font-family: "Open Sans", Arial, sans-serif;
    color: var(--white);
  }
  .backdrop { position: absolute; inset: 0; }
  .title {
    position: absolute;
    top: 578px;
    left: 0;
    width: 100%;
    text-align: center;
    font-family: "Emilys Candy", cursive;
    font-weight: 400;
    font-size: 112px;
    line-height: 1;
    color: var(--peach);
    letter-spacing: 8px;
  }
  .date-bar {
    position: absolute;
    top: 701px;
    left: 183px;
    width: 549px;
    height: 42px;
    background: var(--olive);
    border-radius: 4px;
    text-align: center;
    font-weight: 700;
    font-size: 23px;
    line-height: 42px;
  }
  .details {
    position: absolute;
    top: 770px;
    left: 30px;
    width: 873px;
    text-align: center;
    font-size: 17px;
    line-height: 24px;
  }
  .details p + p { margin-top: 24px; }
  .brand {
    position: absolute;
    top: 1068px;
    left: 62px;
    display: flex;
    align-items: center;
    gap: 12px;
    font-weight: 700;
    font-size: 26px;
    color: var(--olive);
  }
  .brand-dot {
    width: 42px;
    height: 42px;
    border-radius: 50%;
    background: var(--orange);
  }
  .reservations {
    position: absolute;
    top: 1080px;
    left: 578px;
    width: 312px;
    text-align: center;
    font-family: "Amatic SC", cursive;
    font-weight: 700;
    font-size: 38px;
    line-height: 1;
    color: var(--peach);
    letter-spacing: 1px;
  }
  .info-bar {
    position: absolute;
    top: 1138px;
    left: 36px;
    width: 860px;
    height: 38px;
    border-radius: 19px;
    background: var(--olive);
    box-shadow: 0 0 0 3px var(--olive-light);
    display: flex;
    align-items: center;
    padding: 0 34px;
    font-size: 17px;
  }
  .info-bar .web { display: flex; align-items: center; gap: 7px; }
  .info-bar .web strong { font-weight: 700; }
  .info-bar .divider { width: 2px; height: 26px; background: #b9c27a; margin: 0 18px 0 20px; }
  .info-bar .address { display: flex; align-items: center; gap: 7px; }
  .badge {
    position: absolute;
    left: 741px;
    top: 390px;
    width: 180px;
    height: 180px;
    border-radius: 50%;
    background: var(--olive);
    box-shadow: 0 0 0 4px var(--white), 0 0 0 7px var(--peach);
    display: flex;
    flex-direction: column;
    align-items: center;
    justify-content: center;
    font-family: "Amatic SC", cursive;
    font-weight: 700;
    text-align: center;
    line-height: 1;
  }
  .badge .small { font-size: 25px; letter-spacing: 1px; }
  .badge .big { font-size: 50px; letter-spacing: 2px; margin-top: 4px; }
</style>
</head>
<body>
<div class="flyer">
  <svg class="backdrop" width="933" height="1200" viewBox="0 0 933 1200">
    <defs>
      <linearGradient id="sceneTone" x1="0" y1="0" x2="1" y2="0">
        <stop offset="0" stop-color="#e6ebe4"/>
        <stop offset="0.22" stop-color="#d8c7b6"/>
        <stop offset="0.42" stop-color="#c4b7a6"/>
        <stop offset="0.55" stop-color="#3b3a36"/>
        <stop offset="0.76" stop-color="#45423b"/>
        <stop offset="0.88" stop-color="#dfe4dc"/>
        <stop offset="1" stop-color="#e8ece6"/>
      </linearGradient>
      <linearGradient id="sceneShade" x1="0" y1="0" x2="0" y2="1">
        <stop offset="0" stop-color="#ffffff" stop-opacity="0"/>
        <stop offset="0.7" stop-color="#ffffff" stop-opacity="0"/>
        <stop offset="1" stop-color="#a0775a" stop-opacity="0.55"/>
      </linearGradient>
      <radialGradient id="bookGlow" cx="0.5" cy="0.55" r="0.5">
        <stop offset="0" stop-color="#fbeedd"/>
        <stop offset="0.6" stop-color="#f6dfc6"/>
        <stop offset="1" stop-color="#f6dfc6" stop-opacity="0"/>
      </radialGradient>
    </defs>

    <path class="band-olive" d="M0 400 L933 340 L933 420 Q 650 560 300 545 Q 120 538 0 470 Z" fill="var(--olive)"/>

    <g role="img" aria-label="Photo of a smiling storyteller holding a children's picture book beside a storytime welcome chalkboard, a plush frog and toy trains, with a kite and bunting over a pale storybook-pattern wall">
      <path d="M0 0 H933 V360 Q 560 650 0 420 Z" fill="url(#sceneTone)"/>
      <path d="M0 0 H933 V360 Q 560 650 0 420 Z" fill="url(#sceneShade)"/>
    </g>

    <path class="band-orange" d="M0 462 Q 300 590 640 520 Q 800 480 933 400 L933 1200 L0 1200 Z" fill="var(--orange)"/>
    <path class="swoosh-soft" d="M933 420 Q 760 520 690 640 Q 640 760 680 900 Q 760 860 933 860 Z" fill="var(--orange-soft)" opacity="0.45"/>
    <path class="wave-soft" d="M560 1200 C 600 1080, 720 975, 933 945 L933 1200 Z" fill="var(--orange-deep)" opacity="0.55"/>
    <path class="corner-white" d="M0 990 C 200 935, 420 965, 515 1060 C 555 1100, 570 1160, 562 1200 L0 1200 Z" fill="var(--white)"/>

    <g role="img" aria-label="Illustration of an open book">
      <ellipse cx="800" cy="1036" rx="82" ry="38" fill="url(#bookGlow)"/>
    </g>
  </svg>

  <div class="badge">
    <span class="small">STORYTIME</span>
    <span class="small">SERIES</span>
    <span class="small">EIGHT-WEEK</span>
    <span class="big">FREE</span>
  </div>

  <h1 class="title">Storytime</h1>

  <div class="date-bar">~~ STARTING AT 10AM ON JULY 7TH~~</div>

  <div class="details">
    <p>At Glow And Grow we believe that the shortest distance between two people is a story.</p>
    <p>Everything in our store has a story behind it and now we are excited to have one of the world’s<br>best storytellers coming to share her gifts with kids ages 2-5, once a week, starting at<br>10am on July 7th for an eight-week series.</p>
    <p>Ms. Dolores (Pemberley), children’s librarian and storyteller extraordinaire, and our own Mr. Toby,<br>her budding apprentice, will regale children with music, stories and movement, FREE!</p>
  </div>

  <div class="brand">
    <span class="brand-dot"></span>
    <span class="brand-name">Glow And Grow</span>
  </div>

  <div class="reservations">Reservations Required!</div>

  <div class="info-bar">
    <span class="web">Visit
      <svg width="16" height="16" viewBox="0 0 16 16" aria-hidden="true"><circle cx="8" cy="8" r="6.5" fill="none" stroke="#fff" stroke-width="1.6"/><path d="M5.5 4.5 C 5 6, 6.5 7, 8 8 C 9.5 9, 10.5 10, 10 11.5" fill="none" stroke="#fff" stroke-width="1.4"/></svg>
      <strong>glowandgrow.example</strong> for details</span>
    <span class="divider"></span>
    <span class="address">
      <svg width="17" height="15" viewBox="0 0 17 15" aria-hidden="true"><path d="M8.5 0 L17 7.5 L14.5 7.5 L14.5 15 L10.5 15 L10.5 10 L6.5 10 L6.5 15 L2.5 15 L2.5 7.5 L0 7.5 Z" fill="#fff"/></svg>
      872 E. 61st Street - San Mateo CA 94417</span>
  </div>
</div>
</body>
</html>
```